Australian Craft Distillery needs poster layout for its awesome Manifesto

Tall Finch's a small craft distillery based in the Brook Flats of Western Australia producing award-winning vodkas and gin. Check out our website www.tallfinchs-example.com.au to get a feel for our design aesthetic, especially from our bottle design. We are "Small Batch Liquors - Out of the Brook Flats". Everything we do reflects that.
We have a manifesto - The Tall Finch's Manifesto -that we proudly display in our tasting room, and was used as a basis for an artwork in our entry.
We've had a number of customers ask to buy a poster of the manifesto (attached) so I want to commission a more professional design than the current layout which was put together in Word! (yes I know, I'm sorry, I did move it into Illustrator later).
I think the text flows in a sequential order so I'm looking for a design that you read from start to finish rather than a random collection of statements. I'd like to include our logo in the design somewhere but it doesn't have to be front and centre. There is a secondary logo device as well - the interlocked T and F on the label which could be used. I'm assuming the print will be simple black on either a plain background or a "craft background" similar to the labels. Our current fonts are SchmutzICG for text and VeneerTwo for headings. The label uses Haymaker and Gin-Rough.
Print size will be A3 (prefer the design to be to this proportion and portrait orientation) and bigger up to A1. We'll print the final design on the back of t-shirts for staff as well. If I was going to sum up our style in a couple of words it would be "intelligently irreverent" Have fun with this, I certainly did writing it!

```html
<!DOCTYPE html>
<html lang="en">
<head>
<meta charset="utf-8">
<title>The Tall Finch's Manifesto</title>
<link rel="stylesheet" href="https://fonts.googleapis.com/css2?family=Alfa+Slab+One&family=Special+Elite&display=swap">
<style>
  :root {
    --page: #ffffff;
    --kraft: #c9a47c;
    --kraft-light: #d8b892;
    --kraft-dark: #b8916a;
    --ink: #231a14;
    --rule: #3a2a1e;
    --accent-green: #8cc63f;
  }
  html, body {
    margin: 0;
    padding: 0;
    width: 849px;
    height: 1200px;
    overflow: hidden;
    background: var(--page);
  }
  .canvas {
    position: relative;
    width: 849px;
    height: 1200px;
  }
  .label {
    position: absolute;
    left: 204px;
    top: 20px;
    width: 440px;
    height: 1160px;
    background: linear-gradient(180deg, var(--kraft-light) 0%, var(--kraft) 40%, var(--kraft-dark) 100%);
    color: var(--ink);
    font-family: "Special Elite", "Courier New", monospace;
    box-sizing: border-box;
  }
  .label__edge {
    position: absolute;
    top: 0;
    bottom: 0;
    width: 16px;
    background: var(--accent-green);
  }
  .label__edge--left { left: 0; }
  .label__edge--right { right: 0; }

  .masthead {
    position: absolute;
    left: 16px;
    right: 16px;
    top: 0;
    height: 168px;
    background: var(--kraft-light);
    border-bottom: 3px solid var(--rule);
    text-align: center;
    box-sizing: border-box;
    padding-top: 36px;
  }
  .masthead__title {
    margin: 0;
    font-family: "Alfa Slab One", Georgia, serif;
    font-weight: 400;
    font-size: 23px;
    letter-spacing: 0.5px;
    text-transform: uppercase;
    line-height: 1;
  }
  .masthead__rule {
    width: 86%;
    margin: 16px auto 14px;
    border: 0;
    border-top: 2px solid var(--rule);
  }
  .masthead__subtitle {
    margin: 0;
    font-size: 17px;
    line-height: 1.35;
    text-transform: uppercase;
    letter-spacing: 0.5px;
  }

  .manifesto {
    position: absolute;
    left: 16px;
    right: 16px;
    top: 168px;
    bottom: 0;
    padding: 20px 14px 0;
    box-sizing: border-box;
    text-align: center;
    font-size: 13px;
    line-height: 1.5;
  }
  .stage {
    padding-bottom: 12px;
    margin-bottom: 14px;
    border-bottom: 1.5px solid var(--rule);
  }
  .stage:last-child { border-bottom: 0; }
  .stage__heading {
    margin: 0 0 4px;
    font-size: 16px;
    font-weight: 400;
  }
  .stage__list {
    list-style: none;
    margin: 0;
    padding: 0;
  }
</style>
</head>
<body>
<div class="canvas">
  <article class="label">
    <div class="label__edge label__edge--left"></div>
    <div class="label__edge label__edge--right"></div>

    <header class="masthead">
      <h1 class="masthead__title">The Tall Finch's Manifesto</h1>
      <hr class="masthead__rule">
      <p class="masthead__subtitle">Our thoughts on life,<br>a.k.a. how to be better</p>
    </header>

    <section class="manifesto">
      <div class="stage">
        <h2 class="stage__heading">First...</h2>
        <ul class="stage__list">
          <li>• Work Smart • Love Hard • Play Often •</li>
          <li>• Sleep More •</li>
          <li>• Stay Present • Be Loyal • Embrace Silly •</li>
          <li>• Get Dirty Stuff Stay Clean •</li>
          <li>• Laugh • Cry • Win • Dance • Sing •</li>
          <li>• Stop That Last Slow Ease •</li>
        </ul>
      </div>

      <div class="stage">
        <h2 class="stage__heading">Then...</h2>
        <ul class="stage__list">
          <li>• Celebrate others success • Don't be shit •</li>
          <li>• Have one thing you are awesome at •</li>
          <li>• Get off your phone •</li>
          <li>• Share some real passion •</li>
          <li>• Make something •</li>
          <li>• Making money doesn't count •</li>
          <li>• Healing takes time •</li>
          <li>• Never stop exploring, never stop learning,</li>
          <li>share that with others •</li>
          <li>• We all f*ck up •</li>
          <li>Make good, learn, be better and move on •</li>
          <li>• Life is far too short,</li>
          <li>squeeze every drop out of it -</li>
          <li>and, of course ... •</li>
          <li>• Drink better •</li>
        </ul>
      </div>

      <div class="stage">
        <h2 class="stage__heading">and finally ...</h2>
        <ul class="stage__list">
          <li>• Sometimes you just won't understand •</li>
          <li>• Be composed in a fight •</li>
          <li>• You are not as important as you think •</li>
          <li>• You are more loved than you think •</li>
          <li>• Dare to do things alone •</li>
          <li>• Be slow to be busy •</li>
          <li>• There is no good reason to do</li>
          <li>a half arsed job •</li>
          <li>• Teaching is the best way of learning •</li>
          <li>• The past is important, what you do</li>
          <li>next is more so •</li>
          <li>• Change is inevitable, roll with it •</li>
          <li>• Success is whatever you decide it to be •</li>
        </ul>
      </div>
    </section>
  </article>
</div>
</body>
</html>
```